we do all sorts of cleaning however bookings are limited!
why not chose the right cleaners for you!
pressure cleaning, window cleaning, office, end of lease clean, accommodation, industrial and commercial cleaning and house cleaning

Logo Text

Bright Nest Cleaning Service

```html
<!DOCTYPE html>
<html lang="en">
<head>
<meta charset="utf-8">
<title>Bright Nest Cleaning Service – Business Card</title>
<link href="https://fonts.googleapis.com/css2?family=Poppins:wght@400;600;700&display=swap" rel="stylesheet">
<style>
  :root {
    --backdrop: #e4e4e4;
    --card-white: #ffffff;
    --brand-blue: #1ca8e6;
    --brand-green: #7cc242;
    --text-grey: #555555;
    --divider: #bdbdbd;
    --back-top: #00b4f0;
    --back-bottom: #04a8ec;
    --back-mark: #3fd8f7;
  }
  * { box-sizing: border-box; margin: 0; padding: 0; }
  html, body {
    width: 1200px; height: 1200px; overflow: hidden;
    background: var(--backdrop);
    font-family: "Poppins", sans-serif;
  }
  .canvas { position: relative; width: 1200px; height: 1200px; }
  .card {
    position: absolute;
    width: 688px; height: 393px;
    border-radius: 22px;
    overflow: hidden;
  }
  .card-front { left: 267px; top: 158px; background: var(--card-white); }
  .card-back {
    left: 262px; top: 652px;
    background: linear-gradient(180deg, var(--back-top), var(--back-bottom));
  }

  .brand {
    position: absolute;
    display: flex; align-items: center; gap: 10px;
    color: var(--brand-blue);
    font-weight: 600;
  }
  .brand-dot { border-radius: 50%; background: currentColor; flex: none; }
  .brand-text { display: flex; flex-direction: column; line-height: 1; }
  .brand-name { letter-spacing: -0.5px; }
  .brand-tagline { text-transform: uppercase; letter-spacing: 1px; }

  .card-front .brand { left: 82px; top: 166px; }
  .card-front .brand-dot { width: 14px; height: 14px; }
  .card-front .brand-name { font-size: 40px; }
  .card-front .brand-tagline { font-size: 11px; margin-top: 6px; text-align: right; }

  .divider {
    position: absolute; left: 358px; top: 115px;
    width: 1.5px; height: 164px;
    background: linear-gradient(180deg, transparent, var(--divider) 15%, var(--divider) 85%, transparent);
  }
  .person { position: absolute; left: 391px; top: 114px; }
  .person-name {
    font-size: 25px; font-weight: 700; color: var(--brand-blue);
    line-height: 1.1; letter-spacing: 0.3px;
  }
  .person-title { font-size: 15px; color: var(--text-grey); margin-top: 2px; }

  .contact-list { position: absolute; left: 396px; top: 179px; list-style: none; }
  .contact-item {
    display: flex; align-items: center; gap: 10px;
    height: 21px; font-size: 17px; color: var(--text-grey);
    line-height: 1;
  }
  .contact-icon { width: 14px; height: 14px; flex: none; fill: var(--brand-green); }

  .address {
    position: absolute; left: 0; right: 0; top: 339px;
    text-align: center; font-size: 17px; color: var(--text-grey);
  }

  .card-back .brand {
    left: 50%; top: 50%; transform: translate(-50%, -50%);
    color: var(--back-mark); gap: 16px;
  }
  .card-back .brand-dot { width: 22px; height: 22px; }
  .card-back .brand-name { font-size: 72px; }
  .card-back .brand-tagline { font-size: 19px; margin-top: 8px; text-align: right; }
</style>
</head>
<body>
<main class="canvas">
  <section class="card card-front">
    <div class="brand">
      <span class="brand-dot"></span>
      <div class="brand-text">
        <span class="brand-name">Bright Nest</span>
        <span class="brand-tagline">Cleaning Service</span>
      </div>
    </div>

    <div class="divider"></div>

    <div class="person">
      <h1 class="person-name">DANIEL REYES</h1>
      <p class="person-title">President</p>
    </div>

    <ul class="contact-list">
      <li class="contact-item">
        <svg class="contact-icon" viewBox="0 0 16 16"><path d="M3.5 1l2.5 3-1.5 2c.8 2 2.5 3.7 4.5 4.5l2-1.5 3 2.5-1.5 2.5C7 15 1 9 1 2.5z"/></svg>
        <span>555-210-4871</span>
      </li>
      <li class="contact-item">
        <svg class="contact-icon" viewBox="0 0 16 16"><path d="M4 0h8a1 1 0 0 1 1 1v14a1 1 0 0 1-1 1H4a1 1 0 0 1-1-1V1a1 1 0 0 1 1-1zm1 2v10h6V2zm3 11a1 1 0 1 0 0 2 1 1 0 0 0 0-2z"/></svg>
        <span>555-392-6018</span>
      </li>
      <li class="contact-item">
        <svg class="contact-icon" viewBox="0 0 16 16"><path d="M1 3h14v10H1zm1.5 1.5v.3L8 9l5.5-4.2v-.3zm0 2.2v4.8h11V6.7L8 10.9z"/></svg>
        <span>hello@brightnestclean.com</span>
      </li>
      <li class="contact-item">
        <svg class="contact-icon" viewBox="0 0 16 16"><circle cx="8" cy="8" r="7"/><path d="M5 4c2 1 1 3 3 3s1 3 0 4M10 3c-1 2 2 2 3 3" stroke="#fff" stroke-width="1.3" fill="none"/></svg>
        <span>www.brightnestclean.com</span>
      </li>
    </ul>

    <p class="address">412 Willowbank Road, Fairview, Canada 20418</p>
  </section>

  <section class="card card-back">
    <div class="brand">
      <span class="brand-dot"></span>
      <div class="brand-text">
        <span class="brand-name">Bright Nest</span>
        <span class="brand-tagline">Cleaning Service</span>
      </div>
    </div>
  </section>
</main>
</body>
</html>
```